Brantel Power Core Values Poster

We want to display our company core values around our business. we want a poster that lists them with some cool solar graphics attached. This is to inspire and motivate our employees, promote our company and continue to adhere to a high code of conduct.

kladsf al asa kajdlkj akdj afa sdlkdjalk a dj faklsdoejsd poj dfoperjeo aod sd oe e oeoee fr oeoeo oee oeoeoe eooeoeoe eoeoeoeododoeoo dd d od d o d dddo doododo do dodododo do do doododo dodo odododododo dododoododododododododood ododo dododo

Target Market(s)

Employees

Industry/Entity Type

Solar Energy

Font styles to use
Serif

Colors
3176b5

Requirements
Must have
• All of the listed content in core values document. Can be multiple posters
Nice to have
• inspirational pictures
Should not have
• N/A

```html
<!DOCTYPE html>
<html lang="en">
<head>
<meta charset="utf-8">
<title>Brantel Power — Core Values Poster</title>
<link rel="stylesheet" href="https://fonts.googleapis.com/css2?family=Oswald:wght@300;400;600;700&family=Open+Sans:ital,wght@1,300&display=swap">
<style>
  :root {
    --sky-top: #b8a7c7;
    --sky-mid: #d8c5d0;
    --sky-glow: #ebcfae;
    --horizon: #d9a874;
    --field-dark: #3e2a26;
    --field-mid: #6b4a3c;
    --brand-blue: #2f3b90;
    --brand-blue-deep: #26327f;
    --band-blue: #3442a0;
    --logo-blue: #5160ac;
    --tagline-green: #c9d13e;
    --headline-light: #f4eee7;
    --body-white: #ffffff;
  }
  html, body {
    margin: 0;
    padding: 0;
    width: 873px;
    height: 1200px;
    overflow: hidden;
    background: #ffffff;
  }
  .poster {
    position: relative;
    width: 873px;
    height: 1200px;
    overflow: hidden;
    font-family: "Oswald", "Arial Narrow", sans-serif;
  }
  .poster__scene {
    position: absolute;
    inset: 0;
    background: linear-gradient(180deg,
      var(--sky-top) 0%,
      var(--sky-mid) 28%,
      var(--sky-glow) 46%,
      var(--horizon) 52%,
      var(--field-mid) 58%,
      var(--field-dark) 75%,
      var(--field-dark) 100%);
  }
  .poster__swoosh {
    position: absolute;
    inset: 0;
    width: 873px;
    height: 1200px;
  }
  .brand {
    position: absolute;
    left: 124px;
    top: 150px;
  }
  .brand__name {
    margin: 0;
    font-weight: 600;
    font-size: 86px;
    line-height: 1;
    letter-spacing: 1px;
    color: var(--logo-blue);
  }
  .brand__tagline {
    margin: 4px 0 0;
    font-family: "Open Sans", "Helvetica", sans-serif;
    font-style: italic;
    font-weight: 300;
    font-size: 22px;
    color: var(--tagline-green);
  }
  .value {
    position: absolute;
    left: 181px;
    top: 428px;
  }
  .value__title {
    margin: 0;
    font-weight: 700;
    font-size: 88px;
    line-height: 1;
    color: var(--brand-blue);
    text-shadow: 1px 2px 2px rgba(0,0,0,0.35);
  }
  .value__motto {
    margin: -2px 0 0 237px;
    font-weight: 300;
    font-size: 40px;
    line-height: 1.1;
    color: var(--brand-blue);
    white-space: nowrap;
  }
  .statement {
    position: absolute;
    right: 69px;
    text-align: right;
    color: var(--body-white);
  }
  .statement--mission { top: 770px; }
  .statement--vision { top: 975px; }
  .statement__title {
    margin: 0;
    font-weight: 700;
    font-size: 112px;
    line-height: 1;
    color: var(--headline-light);
    text-shadow: 2px 3px 4px rgba(0,0,0,0.45);
  }
  .statement__text {
    margin: 6px 0 0;
    font-weight: 400;
    font-size: 17.5px;
    line-height: 21px;
    letter-spacing: -0.2px;
    text-shadow: 1px 1px 2px rgba(0,0,0,0.5);
  }
</style>
</head>
<body>
<main class="poster">
  <div class="poster__scene" role="img" aria-label="Photograph of a solar carport array on a farm at sunset, with barns, trees and a glowing sun in a lavender sky"></div>

  <svg class="poster__swoosh" viewBox="0 0 873 1200" aria-hidden="true">
    <path d="M873,458 C800,700 600,950 0,1008 L0,1028 C610,975 820,730 873,480 Z" fill="var(--band-blue)"/>
    <path d="M873,418 C810,700 600,960 0,1032 L0,1050 C620,990 830,720 873,452 Z" fill="var(--brand-blue)" opacity="0"/>
    <path d="M873,500 C790,760 560,1010 0,1062 L0,1200 L873,1200 Z" fill="var(--brand-blue)"/>
    <path d="M873,418 C835,600 760,700 690,770 C770,720 840,600 873,460 Z" fill="var(--band-blue)"/>
  </svg>

  <header class="brand">
    <h1 class="brand__name">Brantel Power</h1>
    <p class="brand__tagline">Turning Sunlight Into Savings</p>
  </header>

  <section class="value">
    <h2 class="value__title">Integrity</h2>
    <p class="value__motto">Do the right thing</p>
  </section>

  <section class="statement statement--mission">
    <h2 class="statement__title">Mission</h2>
    <p class="statement__text">Provide our customers with the highest quality, renewable<br>energy products and services to maximize their savings and<br>give them the freedom to power anything, anywhere.</p>
  </section>

  <section class="statement statement--vision">
    <h2 class="statement__title">Vision</h2>
    <p class="statement__text">Continue to be a full service renewable energy company providing<br>solar, battery storage, off-grid, service, and maintenance solutions.</p>
  </section>
</main>
</body>
</html>
```